Service Menu refresh 2018 Update of menu pricing

We currently have service menus as attached. We will be updating our look via our homepage image, our service menu and our in-house beverage and treatment menu.
We are a natural and sustainable hair salon group and moving more towards head spa which consists of treatments, beauty, tanning as well as your traditional hair services. Our imagery needs to reflect our efforts in spa treatments in the hair and scalp area and use natural materials and colours reflecting sustainability.
Velin is the brand we stock and promote.

Target Market(s)

Men or women interesting in personal maintenance with natural and organic products and using sustainable practises

Industry/Entity Type

Hair And Beauty

Font styles to use
Sans Serif
Other font styles liked:
• Arial or Helvetica

Colors
9acb3c
abd037
cadf82
ffffff

Requirements
Must have
• Name on the front cover, locations on back cover
Nice to have
• Prestige feel, reflect male and female clients
Should not have
• Bold artificial writing or any type of cartoon images.
• Same images as existing menu.

```html
<!DOCTYPE html>
<html lang="en">
<head>
<meta charset="utf-8">
<title>Fernleaf Hair Studios – Service Menu</title>
<link href="https://fonts.googleapis.com/css2?family=Arimo:ital,wght@0,400;0,700;1,700&display=swap" rel="stylesheet">
<style>
:root{
  --green:#9acb3c;
  --lime:#abd037;
  --pale:#cadf82;
  --white:#ffffff;
  --ink:#3a3a3a;
  --grey-head:#8a8c8e;
  --cell:#ececec;
  --stage:#e6e7e9;
}
*{box-sizing:border-box;margin:0;padding:0}
html,body{width:807px;height:1200px;overflow:hidden}
body{background:var(--stage);font-family:"Arimo",Arial,sans-serif;color:var(--ink);position:relative}

.page{position:absolute;width:370px;height:370px;background:var(--white);box-shadow:0 2px 6px rgba(0,0,0,.12);overflow:hidden}

/* back cover */
.back-cover{left:25px;top:110px;padding:26px 26px 20px}
.quote{font-weight:700;font-style:italic;font-size:15px;line-height:18px;margin-bottom:12px}
.location{margin-bottom:6px}
.location h3{color:var(--green);font-size:9px;font-weight:700;text-transform:uppercase;line-height:11px}
.location p{font-size:8px;line-height:10.5px;display:flex;align-items:center;gap:4px}
.location svg{width:7px;height:7px;fill:var(--green);flex:none}
.site{color:var(--green);font-size:13px;font-weight:700;margin-top:8px;letter-spacing:.3px}

/* front cover */
.front-cover{left:412px;top:110px}
.cover-photo{position:absolute;inset:0;background:linear-gradient(165deg,#f3f8e8 0%,#dcebb9 50%,#b9d37e 82%,#8f7356 100%)}
.brand{position:absolute;left:0;right:0;top:120px;display:flex;align-items:center;justify-content:center;gap:6px}
.brand-dot{width:10px;height:10px;border-radius:50%;background:var(--green)}
.brand-name{font-size:16px;font-weight:700;color:var(--ink)}

/* inside spread */
.spread{position:absolute;left:33px;top:660px;width:740px;height:370px;box-shadow:0 2px 6px rgba(0,0,0,.12)}
.spread .page{position:absolute;top:0;box-shadow:none;padding:22px 20px}
.spread .left{left:0;border-right:1px solid #e2e2e2}
.spread .right{left:370px}
.price-table{width:100%;border-collapse:separate;border-spacing:1px;font-size:8px}
.price-table th{background:var(--grey-head);color:var(--white);font-size:9px;height:16px;width:36px}
.price-table th.blank{background:none}
.price-table td{height:14px;padding:0 4px;vertical-align:middle}
.price-table td.price{background:var(--cell);text-align:center;width:36px}
.price-table td.name{font-weight:700;text-transform:uppercase}
.price-table tr.section td{background:var(--lime);color:var(--white);font-weight:700;font-size:10px;height:16px;text-transform:uppercase}
.price-table tr.section.soft td{background:var(--pale);color:var(--ink)}
.notes{font-size:7px;line-height:9px;margin-top:6px}
.footnote{position:absolute;left:20px;right:20px;bottom:18px;font-size:7.5px;line-height:10px}
</style>
</head>
<body>

<svg width="0" height="0" style="position:absolute">
  <symbol id="icon-pin" viewBox="0 0 10 10"><path d="M5 0a3.5 3.5 0 0 1 3.5 3.5C8.5 6 5 10 5 10S1.5 6 1.5 3.5A3.5 3.5 0 0 1 5 0zm0 2a1.5 1.5 0 1 0 0 3a1.5 1.5 0 0 0 0-3z"/></symbol>
  <symbol id="icon-phone" viewBox="0 0 10 10"><path d="M2 0l2 2.5-1 1.2a6 6 0 0 0 3.3 3.3l1.2-1L10 8l-1 2C4 10 0 6 0 1z"/></symbol>
  <symbol id="icon-mail" viewBox="0 0 10 10"><path d="M0 2h10v6H0zM1 3v.3l4 2.5 4-2.5V3z"/></symbol>
</svg>

<section class="page back-cover" aria-label="Back cover">
  <p class="quote">“Living a more natural and organic life is a philosophy not just a product certification”</p>

  <div class="location"><h3>Brookvale</h3>
    <p><svg><use href="#icon-pin"/></svg>Shop 1018 Brookvale Plaza, Creek Rd, Brookvale</p>
    <p><svg><use href="#icon-phone"/></svg>+61 (07) 3000 1101</p>
    <p><svg><use href="#icon-mail"/></svg>brookvale@fernleafhair.com.au</p></div>

  <div class="location"><h3>Kelmore</h3>
    <p><svg><use href="#icon-pin"/></svg>Shop 231 Kelmore Plaza, Miller Road, Kelmore</p>
    <p><svg><use href="#icon-phone"/></svg>+61 (07) 3000 1102</p>
    <p><svg><use href="#icon-mail"/></svg>kelmore@fernleafhair.com.au</p></div>

  <div class="location"><h3>In Tarrawood</h3>
    <p><svg><use href="#icon-pin"/></svg>Shop 3082 Tarrawood Shopping Centre, Banksia Rd</p>
    <p><svg><use href="#icon-phone"/></svg>+61 (07) 3000 1103</p>
    <p><svg><use href="#icon-mail"/></svg>tarrawood@fernleafhair.com.au</p></div>

  <div class="location"><h3>Southwater</h3>
    <p><svg><use href="#icon-pin"/></svg>Shop 1255 Southwater Plaza, Harbour St, Southwater</p>
    <p><svg><use href="#icon-phone"/></svg>+61 (07) 3000 1104</p>
    <p><svg><use href="#icon-mail"/></svg>southwater@fernleafhair.com.au</p></div>

  <div class="location"><h3>Riverbend Medical Centre</h3>
    <p><svg><use href="#icon-pin"/></svg>Larkspur St, Parkfield QLD 4000</p>
    <p><svg><use href="#icon-phone"/></svg>+61 (07) 3000 1105</p>
    <p><svg><use href="#icon-mail"/></svg>riverbend@fernleafhair.com.au</p></div>

  <p class="site">WWW.FERNLEAFHAIR.COM.AU</p>
</section>

<section class="page front-cover" aria-label="Front cover">
  <div class="cover-photo" role="img" aria-label="Photograph of a wreath of tropical leaves over soft green bokeh, with stacked spa pebbles and bamboo sprigs on a wooden surface"></div>
  <div class="brand"><span class="brand-dot"></span><span class="brand-name">fernleaf</span></div>
</section>

<section class="spread" aria-label="Inside price menu">
  <div class="page left">
    <table class="price-table">
      <tr><th class="blank"></th><th>S</th><th>M</th><th>L</th><th>XL</th></tr>
      <tr class="section"><td colspan="5">Cut &amp; Blowdry</td></tr>
      <tr><td class="name">Ladies</td><td class="price"></td><td class="price">$88</td><td class="price">$99</td><td class="price">$110</td></tr>
      <tr><td class="name">Fringe</td><td class="price">$15</td><td class="price"></td><td class="price"></td><td class="price"></td></tr>
      <tr><td>Trim</td><td class="price"></td><td class="price">$55</td><td class="price">$62</td><td class="price">$70</td></tr>
      <tr><td>Restyle &amp; finish</td><td class="price"></td><td class="price">$95</td><td class="price">$105</td><td class="price">$118</td></tr>
      <tr><td class="name">Gents cut</td><td class="price">$45</td><td class="price"></td><td class="price"></td><td class="price"></td></tr>
      <tr><td class="name">Kids under 12</td><td class="price">$30</td><td class="price"></td><td class="price"></td><td class="price"></td></tr>
      <tr class="section soft"><td colspan="5">Blowdry</td></tr>
      <tr><td class="name">Long blowdry</td><td class="price"></td><td class="price">$57</td><td class="price">$67</td><td class="price">$77</td></tr>
      <tr class="section"><td colspan="5">Treatments</td></tr>
      <tr><td class="name">Scalp ritual</td><td class="price">$45</td><td class="price"></td><td class="price"></td><td class="price"></td></tr>
      <tr><td class="name">Head spa</td><td class="price">$85</td><td class="price"></td><td class="price"></td><td class="price"></td></tr>
    </table>
    <p class="footnote">*Price taken for each service. You will ALWAYS receive a firm price after your consultation.<br>S: to the collarbone | L: to the bra strap | XL: past bra strap</p>
  </div>

  <div class="page right">
    <table class="price-table">
      <tr><th class="blank"></th><th>S</th><th>M</th><th>L</th><th>XL</th></tr>
      <tr class="section"><td colspan="5">Colour</td></tr>
      <tr><td class="name">Regrowth</td><td class="price">$83</td><td class="price">$145</td><td class="price">$165</td><td class="price">$185</td></tr>
      <tr><td class="name">Full colour tint</td><td class="price">$125</td><td class="price">$185</td><td class="price">$209</td><td class="price">$225</td></tr>
      <tr><td class="name">Regrowth lightening*</td><td class="price">$165</td><td class="price">$275</td><td class="price">$375</td><td class="price">$475</td></tr>
      <tr><td class="name">Balayage/Ombre*</td><td class="price"></td><td class="price">$175</td><td class="price">$195</td><td class="price">$205</td></tr>
      <tr class="section soft"><td colspan="5">Velin Gloss</td></tr>
      <tr><td class="name">Regrowth</td><td class="price">$99</td><td class="price"></td><td class="price"></td><td class="price"></td></tr>
      <tr><td class="name">Full colour tint</td><td class="price">$155</td><td class="price"></td><td class="price"></td><td class="price"></td></tr>
      <tr class="section"><td colspan="5">Foils*</td></tr>
      <tr><td class="name">Single*</td><td class="price">$11</td><td class="price">$13</td><td class="price">$17</td><td class="price">$22</td></tr>
      <tr><td class="name">1/4 Head</td><td class="price">$135</td><td class="price">$155</td><td class="price">$175</td><td class="price">$195</td></tr>
      <tr><td class="name">1/2 Head</td><td class="price">$185</td><td class="price">$205</td><td class="price">$235</td><td class="price">$265</td></tr>
      <tr><td class="name">Full Head</td><td class="price">$225</td><td class="price">$265</td><td class="price">$315</td><td class="price">$355</td></tr>
      <tr class="section soft"><td colspan="5">Straight</td></tr>
      <tr><td class="name">Keratin straightening system</td><td class="price">$365</td><td class="price">$445</td><td class="price">$535</td><td class="price">$565</td></tr>
    </table>
    <p class="notes">*Includes colour match &amp; toner<br>*Minimum 6 foils without colour<br>*Minimum charge on a Sunday is $40</p>
  </div>
</section>

</body>
</html>
```